Graphic Banner Design - 2.5' x 6' - High Tech Company

We are in need of a banner design for an outdoor sign that will be used at sponsorship events.

Size
2.5' x 6'

The company is a high tech company, and the design will be used for action sports events. So lining up to that would be good.

Tag line to be incorporated...
"Extreme IT Services for Extreme Needs."

Target Market(s)

Business Owners, Entrepreneurs, IT Professionals.

Industry/Entity Type

Information Technology

Logo Text

Brindlex

Colors

Designer to choose colors to be used in the design.

Requirements
Must have
• Must feel young and vibrant, fit in to an action sports event and just be out of this world awesome.
• In the world of the IT, we are the Castavelli. Fast, Awesome, not necessarily cheap, but you know it will do what you want extremely well. Not for everyone, but always desired.

```html
<!DOCTYPE html>
<html lang="en">
<head>
<meta charset="utf-8">
<title>Brindlex – Extreme IT Services Banner</title>
<link rel="stylesheet" href="https://fonts.googleapis.com/css2?family=Montserrat:wght@500&family=Roboto+Condensed:wght@700&display=swap">
<style>
  :root {
    --canvas-bg: #ffffff;
    --stage-dark: #141a3a;
    --stage-mid: #3a3f7a;
    --stage-light: #8a9ad0;
    --crowd-light: #fafafa;
    --crowd-mid: #e6e6e6;
    --band-grey: #5e5e60;
    --navy: #101c38;
    --navy-soft: #1d3563;
    --accent-blue: #3a5fae;
    --accent-blue-deep: #2c4a94;
    --brand-blue: #3d5ca8;
    --headline-grey: #6b6566;
  }
  html, body {
    margin: 0;
    padding: 0;
    overflow: hidden;
    background: var(--canvas-bg);
  }
  .banner {
    position: relative;
    width: 1200px;
    height: 500px;
    overflow: hidden;
    background: var(--canvas-bg);
  }
  .banner-shapes {
    position: absolute;
    inset: 0;
    display: block;
  }
  .brand-name {
    position: absolute;
    left: 700px;
    width: 320px;
    top: 140px;
    margin: 0;
    text-align: center;
    font-family: "Montserrat", sans-serif;
    font-weight: 500;
    font-size: 36px;
    color: var(--brand-blue);
    letter-spacing: 0.5px;
  }
  .tagline {
    position: absolute;
    left: 560px;
    width: 580px;
    top: 236px;
    margin: 0;
    text-align: center;
    font-family: "Roboto Condensed", sans-serif;
    font-weight: 700;
    font-size: 58px;
    line-height: 60px;
    letter-spacing: 1px;
    text-transform: uppercase;
    color: var(--headline-grey);
  }
</style>
</head>
<body>
  <div class="banner">
    <svg class="banner-shapes" width="1200" height="500" viewBox="0 0 1200 500" xmlns="http://www.w3.org/2000/svg">
      <defs>
        <linearGradient id="stage-glow" x1="0" y1="0" x2="0.6" y2="1">
          <stop offset="0" stop-color="var(--stage-dark)"/>
          <stop offset="0.3" stop-color="var(--stage-light)"/>
          <stop offset="0.55" stop-color="var(--stage-mid)"/>
          <stop offset="1" stop-color="var(--stage-dark)"/>
        </linearGradient>
        <linearGradient id="crowd-fade" x1="0" y1="0" x2="0" y2="1">
          <stop offset="0" stop-color="var(--crowd-light)"/>
          <stop offset="1" stop-color="var(--crowd-mid)"/>
        </linearGradient>
        <linearGradient id="navy-corner" x1="0" y1="0" x2="1" y2="1">
          <stop offset="0" stop-color="var(--navy)"/>
          <stop offset="1" stop-color="var(--navy-soft)"/>
        </linearGradient>
      </defs>

      <polygon class="crowd-backdrop" role="img" aria-label="Faint photo of a concert crowd with raised hands"
               points="280,0 1200,0 1200,500 600,500" fill="url(#crowd-fade)"/>

      <polygon class="concert-photo" role="img" aria-label="Photo of a rock band playing on a lit stage in front of a crowd"
               points="0,0 250,0 570,500 0,500" fill="url(#stage-glow)"/>

      <polygon class="corner-navy" points="280,0 492,0 389,170" fill="url(#navy-corner)"/>

      <polygon class="corner-blue-left" points="0,300 70,500 0,500" fill="var(--accent-blue-deep)"/>
      <polygon class="corner-blue-bottom" points="400,500 545,500 505,385" fill="var(--accent-blue)"/>

      <polygon class="diagonal-band" points="250,0 280,0 600,500 570,500" fill="var(--band-grey)"/>
    </svg>

    <p class="brand-name">Brindlex</p>
    <h1 class="tagline">Extreme IT Services<br>for Extreme Needs</h1>
  </div>
</body>
</html>
```